Prominent Trial Lawyer need a Brochure Design for his firm

Douglas R. Pembry of The Pembry Law Firm has been successfully trying severe and complex for over 28 years. He holds the largest verdict in the history of South Georgia of $150,000,000.00 before the late Gerald T. Voskin in the Harlow District of the Lower District of Marren. He specializes in sever injuries, whether by auto accident, trucking accident or medical malpractice. He is also well know for his successful trial of business disputes and high net-worth Divorces.
Target Market(s)
Persons who need an aggressive, experienced trial lawyer especially for personal injury, but also for other civil and business matters, high end divorde
Industry/Entity Type
Medical
Contact Information for Business Card
Need to use coloring and logo uplaoded
Requirements
Must have
- 1) biography of principal, Douglas R. Pembry
- 2) what we do
- 3) specific cases handled, with specific outcomes (will be supplied)

```html
<!DOCTYPE html>
<html lang="en">
<head>
<meta charset="utf-8">
<title>The Pembry Law Firm – Trifold Brochure</title>
<link href="https://fonts.googleapis.com/css2?family=Arimo:wght@400;700&family=Raleway:wght@300;400;700&display=swap" rel="stylesheet">
<style>
  :root {
    --red: #e31e24;
    --red-deep: #b5151a;
    --ink: #222222;
    --body: #333333;
    --paper: #ffffff;
    --stone-light: #d9d9d9;
    --stone-mid: #9c9c9c;
    --stone-dark: #5e5e5e;
    --backdrop: #2a2a2a;
    --slogan: #fcd6d6;
  }
  * { box-sizing: border-box; margin: 0; padding: 0; }
  html, body { width: 1200px; height: 800px; overflow: hidden; background: var(--backdrop); }
  .canvas { position: relative; width: 1200px; height: 800px; overflow: hidden; background: var(--backdrop); font-family: "Arimo", Arial, sans-serif; color: var(--body); }

  .sheet { position: absolute; top: 174px; width: 585px; height: 452px; background: var(--paper); display: flex; overflow: hidden; }
  .sheet--outside { left: 10px; }
  .sheet--inside { left: 605px; }

  /* ---------- outside: about panel ---------- */
  .about-panel { width: 200px; height: 100%; padding: 16px 12px 10px 14px; overflow: hidden; }
  .about-panel p { font-size: 6.6px; line-height: 1.3; margin-bottom: 10px; color: var(--ink); }

  /* ---------- outside: slogan panel ---------- */
  .slogan-panel { position: relative; width: 195px; height: 100%; background: var(--red); }
  .statue-art { position: absolute; top: 12px; left: 26px; width: 62px; height: 150px; background: linear-gradient(180deg, rgba(120,10,14,.28), rgba(120,10,14,.08)); border-radius: 30px 30px 4px 4px; }
  .slogan { position: absolute; top: 112px; left: 14px; right: 14px; font-family: "Raleway", Arial, sans-serif; font-weight: 300; font-size: 11.5px; line-height: 1.4; text-transform: uppercase; text-align: center; color: var(--slogan); letter-spacing: .3px; }
  .team { position: absolute; top: 232px; left: 12px; right: 12px; background: var(--paper); padding: 3px 3px 0; }
  .team-photo { height: 96px; background: linear-gradient(160deg, #6d6a66 0%, #3c3a39 55%, #8a8480 100%); }
  .team-caption { font-size: 7px; color: var(--paper); background: var(--red); text-align: center; padding: 3px 0 2px; margin: 0 -3px; }
  .contact { position: absolute; left: 12px; right: 12px; bottom: 14px; background: var(--paper); border-radius: 8px; padding: 7px 10px; list-style: none; }
  .contact li { display: flex; align-items: center; gap: 5px; font-size: 7.4px; color: var(--ink); line-height: 1.55; }
  .contact svg { width: 8px; height: 8px; flex: none; }

  /* ---------- outside: cover panel ---------- */
  .cover-panel { position: relative; width: 190px; height: 100%; background: linear-gradient(180deg, #eeeeee 0%, var(--stone-light) 35%, var(--stone-mid) 100%); overflow: hidden; }
  .brand { position: absolute; top: 22px; left: 0; right: 0; text-align: center; }
  .brand-dot { width: 26px; height: 26px; border-radius: 50%; background: var(--red); margin: 0 auto 6px; }
  .brand-name { font-family: "Raleway", Arial, sans-serif; font-weight: 700; font-size: 13px; line-height: 1.1; color: var(--ink); }
  .brand-tag { font-family: "Raleway", Arial, sans-serif; font-weight: 400; font-size: 6.5px; letter-spacing: 1px; color: var(--red); margin-top: 3px; }
  .courthouse { position: absolute; top: 110px; left: 0; right: 0; height: 230px; background: linear-gradient(180deg, #bdbdbd 0%, #8e8e8e 45%, var(--stone-dark) 100%); }
  .cover-swoosh { position: absolute; inset: 0; width: 100%; height: 100%; }
  .cover-slogan { position: absolute; left: 30px; right: 12px; bottom: 36px; font-family: "Raleway", Arial, sans-serif; font-weight: 300; font-size: 10px; line-height: 1.4; text-transform: uppercase; text-align: right; color: var(--slogan); }

  /* ---------- inside ---------- */
  .column { width: 195px; height: 100%; padding: 12px 10px 24px; overflow: hidden; }
  .column p, .column li { font-size: 6.3px; line-height: 1.3; color: var(--body); }
  .column p { margin-bottom: 6px; }
  .column h2 { font-size: 8.6px; font-weight: 700; color: var(--ink); margin: 0 0 5px; }
  .column h2.spaced { margin-top: 12px; }
  .column ul { padding-left: 9px; margin-bottom: 6px; }
  .column ul.plain { list-style: disc; }

  .bio-panel { position: relative; }
  .office-photo { height: 78px; margin: -12px -10px 8px; background: linear-gradient(135deg, #c9c4bb 0%, #8c8378 50%, #5a524a 100%); }
  .bio-intro { display: flex; gap: 6px; }
  .bio-intro p { flex: 1; }
  .portrait { width: 78px; height: 100px; flex: none; background: linear-gradient(180deg, #6b7c8c 0%, #3b4652 100%); }

  .inside-rule { position: absolute; left: 0; right: 0; bottom: 13px; height: 1px; background: var(--ink); }
  .inside-band { position: absolute; left: 0; right: 0; bottom: 0; height: 10px; background: var(--red); }
</style>
</head>
<body>
<div class="canvas">

  <!-- Outside spread -->
  <section class="sheet sheet--outside">
    <div class="about-panel">
      <p>The Pembry Law Firm founded in 1989, the firm practices in business and general civil litigation, personal injury, real estate transaction and litigation,criminal defense, and family law. We love the practice of law and how it can help to resolve your civil and family disputes, to right the wrongs done by others, to protect your constitutional rights if you happened to be accused of a crime, to seek fair monetary compensation if you are entitled to. We at The Pembry Law Firm can ensure that you are best represented in courts utilizing the most up-to-date laws, diligent preparation and insightful understanding of your matter.</p>
      <p>The Pembry Law Firm founded in 1989, the firm practices in business and general civil litigation, personal injury, real estate transaction and litigation,criminal defense, and family law. We love the practice of law and how it can help to resolve your civil and family disputes, to right the wrongs done by others, to protect your constitutional rights if you happened to be accused of a crime, to seek fair monetary compensation if you are entitled to. We at The Pembry Law Firm can ensure that you are best represented in courts utilizing the most up-to-date laws, diligent preparation and insightful understanding of your matter.</p>
      <p>The Pembry Law Firm founded in 1989, the firm practices in business and general civil litigation, personal injury, real estate transaction and litigation,criminal defense, and family law. We love the practice of law and how it can help to resolve your civil and family disputes, to right the wrongs done by others, to protect your constitutional rights if you happened to be accused of a crime, to seek fair monetary compensation if you are entitled to. We at The Pembry Law Firm can ensure that you are best represented in courts utilizing the most up-to-date laws, diligent preparation and insightful understanding of your matter.</p>
      <p>The Pembry Law Firm founded in 1989, the firm practices in business and general civil litigation, personal injury, real estate transaction and litigation,criminal defense, and family law. We love the practice of law and how it can help to resolve your civil and family disputes, to right the</p>
    </div>

    <div class="slogan-panel">
      <div class="statue-art" role="img" aria-label="Faint illustration of the Statue of Liberty"></div>
      <p class="slogan">Whether you are against insurance companies, Summit 500 companies or goverments, we level the field and give you the edge.</p>
      <figure class="team">
        <div class="team-photo" role="img" aria-label="Group photo of the law firm team"></div>
        <figcaption class="team-caption">Our Team</figcaption>
      </figure>
      <ul class="contact">
        <li>
          <svg viewBox="0 0 8 8"><rect width="8" height="8" fill="#e31e24"/><path d="M4 1.3a1.8 1.8 0 0 0-1.8 1.8C2.2 4.5 4 6.8 4 6.8s1.8-2.3 1.8-3.7A1.8 1.8 0 0 0 4 1.3z" fill="#fff"/></svg>
          14 Harrow Lane, Dellmont, GA 30999
        </li>
        <li>
          <svg viewBox="0 0 8 8"><rect width="8" height="8" fill="#e31e24"/><path d="M2 1.5h1.2l.6 1.4-.8.6a4 4 0 0 0 1.5 1.5l.6-.8 1.4.6V6A.6.6 0 0 1 5.9 6.6 4.8 4.8 0 0 1 1.4 2.1.6.6 0 0 1 2 1.5z" fill="#fff"/></svg>
          555-014-2LAW
        </li>
        <li>
          <svg viewBox="0 0 8 8"><rect width="8" height="8" fill="#e31e24"/><rect x="1.5" y="2.3" width="5" height="3.6" fill="none" stroke="#fff" stroke-width=".7"/><path d="M1.5 2.3 4 4.3l2.5-2" fill="none" stroke="#fff" stroke-width=".7"/></svg>
          dpembry@pembrylawfirm.com
        </li>
        <li>
          <svg viewBox="0 0 8 8"><rect width="8" height="8" fill="#e31e24"/><circle cx="4" cy="4" r="2.4" fill="none" stroke="#fff" stroke-width=".7"/><path d="M1.6 4h4.8M4 1.6c-1.2 1.4-1.2 3.4 0 4.8M4 1.6c1.2 1.4 1.2 3.4 0 4.8" fill="none" stroke="#fff" stroke-width=".5"/></svg>
          www.pembrylawfirm.com
        </li>
      </ul>
    </div>

    <div class="cover-panel">
      <div class="courthouse" role="img" aria-label="Black and white photo of a columned courthouse"></div>
      <div class="brand">
        <div class="brand-dot"></div>
        <div class="brand-name">The Pembry<br>Law Firm</div>
        <div class="brand-tag">TRIAL LAWYER</div>
      </div>
      <svg class="cover-swoosh" viewBox="0 0 190 452" preserveAspectRatio="none" aria-hidden="true">
        <path d="M0 215 C40 250 70 330 190 322 L190 452 L0 452 Z" fill="#1c1c1c"/>
        <path d="M0 225 C38 262 72 338 190 332 L190 452 L0 452 Z" fill="#e31e24"/>
      </svg>
      <p class="cover-slogan">Whether you are against insurance companies, Summit 500 companies or goverments, we level the field and give you the edge.</p>
    </div>
  </section>

  <!-- Inside spread -->
  <section class="sheet sheet--inside">
    <div class="column bio-panel">
      <div class="office-photo" role="img" aria-label="Photo of the law office entrance"></div>
      <div class="bio-intro">
        <p>Douglas R. Pembry founded The Pembry Law Firm in 1989 and practices business and civil litigation, personal injury and family law. He has spent the last 28 years trying complex cases</p>
        <div class="portrait" role="img" aria-label="Portrait of Douglas R. Pembry"></div>
      </div>
      <p>including medical malpractice, personal injury, criminal and civil cases. He holds the largest verdict in the Lower District of Marren of $150,000,000.00. Currently he specializes in severe personal injury cases and commercial litigation.</p>
    </div>

    <div class="column">
      <h2>Personal Injury</h2>
      <p>If you or loved ones get injured because of negligence of another, you may be entitled to compensation for your pain and suffering and loss of earnings. We handle injuries caused by automobile accidents, slip and fall, medical malpractice, dog bites, criminal assaults on premises and other types of accidents. We take your injury cases on a contingency basis and you do not have to pay attorneys' fees in advance. Sometimes, we could assist you to secure medical services in case you have no financial ability to afford health care. Please contact us for free evaluation.</p>
      <h2 class="spaced">Insurance Coverage and Bad Faith Suits</h2>
      <h2 class="spaced">General Civil Litigation</h2>
      <p>The term civil litigation encompasses wide array of civil actions. The firm can handle various assignments including but not limited to:</p>
      <ul class="plain">
        <li>Breach of contract</li>
        <li>Real Estate Transaction/Litigation</li>
        <li>Administrative Hearings for licenses</li>
        <li>Name Changes</li>
        <li>Insurance Bad Faith</li>
        <li>Fraud</li>
        <li>Sale and Purchase of Businesses</li>
        <li>Probate and Estate Planning.</li>
      </ul>
      <p>Our office has a dynamic litigation practice with years of experience in State and Federal Courts. Our attorneys have tried many cases to jury verdict in a broad range of subjects including real estate, business, personal injury, and wrongful death.</p>
      <p>We employ state of the art technological tools (e.g., scanning, document organizing software, and extensive computer research capabilities).</p>
      <p>Our litigation philosophy is not to take any case we are not prepared to take to a jury.</p>
    </div>

    <div class="column">
      <h2>Criminal Defense</h2>
      <p>If you, or a friend or family member, have been charged with a crime, an uncertain future lies ahead. It is important to have an attorney who knows what to expect in a criminal case, to explain the process, and to help make informed decisions about the best course of action.</p>
      <p>Our attorneys have represented clients who face all types of criminal charges, including</p>
      <ul class="plain">
        <li>DUI</li>
        <li>Drug-related offenses</li>
        <li>Criminal Internet Offenses</li>
        <li>Traffic violations</li>
        <li>White collar crimes</li>
        <li>Felonies and Misdemeanors</li>
      </ul>
      <p>Our attorneys have extensive experience in trying criminal cases. We will not take any case we are not prepared to take to trial.</p>
      <h2 class="spaced">Real Estate Law</h2>
      <h2 class="spaced">Business Transaction</h2>
      <p>The structure of your business enterprise is important. Should you form a corporation, and LLC or a general or limited partnership? We can explain the differences and help you make a choice.</p>
      <p>Once you've decided, we can form that entity and have you up and running in a matter of days with a tax payer identification number ready to do business.</p>
      <p>The term "business" has as many different meanings as there are people on the planet. Sometimes it is a matter of someone lending another person money. We can draft that promissory note.</p>
      <p>Sometimes it is an employment agreement, a non-competition agreement, or a franchise agreement. We have extensive experience in all these areas as well as commercial and private real estate.</p>
    </div>

    <div class="inside-rule"></div>
    <div class="inside-band"></div>
  </section>

</div>
</body>
</html>
```